Stationery Design Project for Explainer Video Company

We are a company for explainer videos. We are working together with a community consisting of creative people. The vorbilo videos are animated. Please visit our homepage at www.vorbilo-studio.de, we like our Monitor-Logo, so please create a similar stationary to that. you might use the colours and the font (Pacifico or similar)
We need business cards too. We don't need Facsimile
attached is the logo (please don't use chatterbox text)

Target Market(s)

Marketing, SMB

Industry/Entity Type

Business

```html
<!DOCTYPE html>
<html lang="de">
<head>
<meta charset="utf-8">
<title>vorbilo – Briefbogen</title>
<link rel="stylesheet" href="https://fonts.googleapis.com/css2?family=Pacifico&display=swap">
<style>
  :root {
    --backdrop: #ececec;
    --paper: #fbfbfb;
    --brand-red: #c8323a;
    --paper-text: #ffffff;
    --mark-grey: #cfcfcf;
    --mark-square: #b9b9b9;
  }
  html, body {
    margin: 0;
    width: 1200px;
    height: 795px;
    overflow: hidden;
    background: var(--backdrop);
  }
  .letterhead {
    position: absolute;
    left: 330px;
    top: 16px;
    width: 540px;
    height: 763px;
    background: var(--paper);
    box-shadow: 0 2px 10px rgba(0,0,0,0.12);
    overflow: hidden;
    font-family: "Pacifico", cursive;
  }
  .contact-band {
    position: absolute;
    left: 0;
    top: 44px;
    width: 500px;
    height: 30px;
    background: var(--brand-red);
    display: flex;
    align-items: center;
    gap: 16px;
    padding-left: 16px;
    box-sizing: border-box;
    color: var(--paper-text);
    font-size: 10px;
    line-height: 1;
    white-space: nowrap;
  }
  .contact-band .website { font-size: 12px; }
  .brand-tag {
    position: absolute;
    right: 14px;
    top: 24px;
    width: 64px;
    height: 60px;
    background: var(--brand-red);
    border-radius: 10px;
    display: flex;
    flex-direction: column;
    align-items: center;
    justify-content: center;
    gap: 4px;
    color: var(--paper-text);
  }
  .brand-tag .square {
    width: 12px;
    height: 12px;
    background: var(--paper-text);
  }
  .brand-tag .name { font-size: 13px; line-height: 1; }
  .watermark {
    position: absolute;
    right: 30px;
    top: 270px;
    display: flex;
    align-items: center;
    gap: 18px;
    color: var(--mark-grey);
    font-size: 84px;
    line-height: 1;
  }
  .watermark .square {
    width: 64px;
    height: 64px;
    background: var(--mark-square);
    opacity: 0.6;
  }
</style>
</head>
<body>
  <main class="letterhead">
    <div class="contact-band">
      <span class="website">www.vorbilo-studio.de</span>
      <span class="phone">Telefon: +49 (030) 55 21 70</span>
      <span class="email">Lena.Hartmann@vorbilo-studio.de</span>
    </div>
    <div class="brand-tag">
      <span class="square"></span>
      <span class="name">vorbilo</span>
    </div>
    <div class="watermark" aria-hidden="true">
      <span class="square"></span>
      <span class="name">vorbilo</span>
    </div>
  </main>
</body>
</html>
```